Dental Practice Billboard Design

We are a newer dental practice in need of a simple but appealing billboard for our growing dental practice to attract new patients. The practice is owned by husband and wife dentists and is family friendly in a small town in Kentucky. We try to be very friendly and caring to our patients. Would prefer a blue background for the billboard and our tooth logo to be prominent. We are partial to the Patua One font used in the image below but please feel free to tweak it as you deem necessary. The shape of the uppercase D and lowercase g are why we like that font, so fonts with a similarly shaped “D” and “g” would work as well. Please include our phone number (606) 847-3962. Please see our website Harlowfamilydentistry.com for more info on the practice if needed. Thank you! Looking forward to seeing your creation.
Updates

The dimensions will be 12ft x 24ft (3.6576m x 7.3152m). Apologies for not including this in the original prompt. Thank you all for your submissions.

Industry/Entity Type

Dental

Font styles to use
Other font styles liked:
• Patua One

Colors
0054AA
0677BA
7BADD7
CADEEF
E8F1F8
0094D4
00A9DD
6FCCEA
C7EBF8
E9F6FB
00AB8E
00BBA5
67D7C9
C6EFE9
E9F9F6
59FF00
82FF00
B8FF75
E3FFCB
F4FFEA

Requirements
Must have
• Phone number, website, Logo, Practice name “Harlow Family Dentistry”
Should not have
• A tagline or slogan

```html
<!DOCTYPE html>
<html lang="en">
<head>
<meta charset="utf-8">
<title>Harlow Family Dentistry Billboard</title>
<link href="https://fonts.googleapis.com/css2?family=Patua+One&family=Open+Sans:wght@700&display=swap" rel="stylesheet">
<style>
  :root {
    --page-bg: #e9eef5;
    --board-blue: #0b4fc2;
    --ink-white: #ffffff;
    --rule-blue: #7badd7;
    --photo-light: #cadeef;
    --photo-warm: #d9c6ad;
    --photo-deep: #6f8fb0;
  }
  * { margin: 0; padding: 0; box-sizing: border-box; }
  html, body {
    width: 1200px;
    height: 857px;
    overflow: hidden;
    background: var(--page-bg);
  }
  .billboard {
    position: absolute;
    left: 20px;
    top: 138px;
    width: 1160px;
    height: 580px;
    background: var(--board-blue);
    overflow: hidden;
  }
  .team-photo {
    position: absolute;
    left: 70px;
    top: 40px;
    width: 300px;
    height: 410px;
    border-radius: 46% 46% 40% 40% / 30% 30% 24% 24%;
    background: linear-gradient(160deg, var(--photo-light) 0%, var(--photo-warm) 45%, var(--photo-deep) 100%);
    border: 8px solid var(--ink-white);
  }
  .practice-name {
    position: absolute;
    left: 428px;
    top: 48px;
    font-family: "Patua One", serif;
    color: var(--ink-white);
    line-height: 1;
  }
  .practice-name .name-main {
    display: block;
    font-size: 142px;
  }
  .practice-name .name-sub {
    display: block;
    font-size: 68px;
    margin-top: 12px;
    margin-left: -4px;
  }
  .divider {
    position: absolute;
    left: 403px;
    top: 332px;
    width: 684px;
    height: 2px;
    background: linear-gradient(90deg, transparent, var(--rule-blue) 15%, var(--rule-blue) 85%, transparent);
  }
  .website {
    position: absolute;
    left: 406px;
    top: 350px;
    font-family: "Open Sans", sans-serif;
    font-weight: 700;
    font-size: 45px;
    color: var(--ink-white);
    letter-spacing: -0.3px;
  }
  .phone {
    position: absolute;
    left: 0;
    width: 1240px;
    top: 455px;
    text-align: center;
    font-family: "Open Sans", sans-serif;
    font-weight: 700;
    font-size: 86px;
    color: var(--ink-white);
    line-height: 1;
  }
</style>
</head>
<body>
  <main class="billboard">
    <div class="team-photo" role="img" aria-label="Photo of the two dentists in white coats, smiling in the clinic"></div>
    <h1 class="practice-name">
      <span class="name-main">Harlow</span>
      <span class="name-sub">Family Dentistry</span>
    </h1>
    <div class="divider"></div>
    <p class="website">Harlowfamilydentistry.com</p>
    <p class="phone">(606) 847-3962</p>
  </main>
</body>
</html>
```